Design a Mobile App for Landscape Businesses

This project is to design the first three screens for a mobile app for Landscape and Lawncare businesses. This app will serve as a directory for homeowners to locate landscape and lawn care businesses and for landscape businesses and contractors to run their business. See the attached PDF for more information and example
Here is the link to the description https://lnkshrt.example/q7Tz3K

Target Market(s)

Landscape and lawn care business, gardeners, home owners

Industry/Entity Type

Landscape Gardening

Logo Text

Velmarigo

Colors

Designer to choose colors to be used in the design.

```html
<!DOCTYPE html>
<html lang="en">
<head>
<meta charset="utf-8">
<title>Landscape Directory App – Screens</title>
<link href="https://fonts.googleapis.com/css2?family=Montserrat:wght@400;500;600;700&display=swap" rel="stylesheet">
<style>
:root{
  --green:#5f7f12;
  --green-dark:#4c6a0c;
  --green-soft:#dfe4cf;
  --page:#ffffff;
  --screen:#f5f5f3;
  --field:#ebebe6;
  --ink:#2f2f2f;
  --muted:#8a8a84;
  --red:#d8242a;
  --white:#ffffff;
}
*{box-sizing:border-box;margin:0;padding:0}
html,body{width:1200px;height:1090px;overflow:hidden;background:var(--page);font-family:"Montserrat",sans-serif;color:var(--ink)}
.stage{position:relative;width:1200px;height:1090px}
.screen{position:absolute;top:205px;width:340px;height:640px;background:var(--screen);border-radius:18px;overflow:hidden;box-shadow:0 10px 40px rgba(0,0,0,.14)}
.screen--directory{left:45px}
.screen--edit{left:430px}
.screen--profile{left:815px}
.status{position:absolute;top:0;left:0;right:0;height:22px;display:flex;justify-content:space-between;align-items:center;padding:0 12px;font-size:9px;color:var(--green);z-index:3}
.status--light{color:var(--white)}
.battery{display:inline-block;width:18px;height:8px;border:1px solid currentColor;border-radius:2px;vertical-align:middle;margin-left:4px;background:currentColor}
/* directory */
.topbar{position:absolute;top:28px;left:12px;right:12px;height:30px;display:flex;align-items:center;gap:10px}
.search{flex:1;height:28px;border-radius:14px;background:var(--green-soft);font-size:9px;color:var(--muted);display:flex;align-items:center;padding-left:12px;gap:6px}
.listing{position:absolute;left:12px;right:12px;background:var(--white);border:1px solid #c9d3a6;border-radius:6px;overflow:hidden}
.listing--one{top:70px;height:262px}
.listing--two{top:342px;height:290px}
.photo{position:relative;height:150px}
.photo-fill{position:absolute;inset:0}
.photo-fill--lawn{background:linear-gradient(180deg,#8ea6c4 0%,#c9d3dc 40%,#4f7a2b 60%,#3d6a1e 100%)}
.photo-fill--garden{background:linear-gradient(160deg,#3f6e24 0%,#5f8d34 45%,#9b86c4 80%,#7d6aa8 100%)}
.photo-title{position:absolute;left:12px;bottom:34px;color:var(--white);font-weight:700;font-size:16px}
.stars{position:absolute;left:12px;bottom:20px;color:var(--white);font-size:10px;letter-spacing:2px}
.state-pill{position:absolute;left:12px;bottom:2px;background:var(--white);border-radius:9px;font-size:9px;font-weight:700;padding:2px 12px}
.state-pill--open{color:var(--green)}
.state-pill--closed{color:var(--red)}
.heart{position:absolute;right:12px;top:12px}
.ghost-quote{position:absolute;left:50%;top:48px;transform:translateX(-50%);border:1.5px solid var(--white);border-radius:20px;color:var(--white);font-size:12px;font-weight:600;padding:10px 26px;white-space:nowrap}
.owner{position:absolute;left:12px;top:160px;display:flex;gap:8px;align-items:center}
.avatar{width:24px;height:24px;border-radius:50%;background:#c9a24a}
.owner-name{font-size:9px;font-weight:700}
.owner-role{font-size:8px;color:var(--muted)}
.blurb{position:absolute;left:12px;right:50px;top:192px;font-size:8px;line-height:1.45;color:#555}
.ago{position:absolute;right:10px;top:192px;font-size:8px;color:var(--muted)}
.btn-small{position:absolute;left:12px;top:226px;background:var(--green);color:var(--white);font-size:8px;font-weight:600;border-radius:10px;padding:6px 14px}
.fab{position:absolute;right:20px;bottom:18px;width:44px;height:44px;border-radius:50%;background:var(--green);display:flex;align-items:center;justify-content:center;box-shadow:0 4px 10px rgba(0,0,0,.2)}
/* edit profile */
.edit-head{position:absolute;top:32px;left:14px;right:14px;display:flex;align-items:center}
.edit-title{flex:1;text-align:center;font-weight:700;font-size:14px;margin-right:18px}
.form{position:absolute;top:70px;left:16px;right:16px}
.field-label{font-size:8px;color:var(--muted);margin:0 0 3px 4px}
.field{height:28px;border-radius:14px;background:var(--field);font-size:10px;display:flex;align-items:center;justify-content:space-between;padding:0 14px;margin-bottom:8px}
.field--area{height:64px;border-radius:12px}
.row{display:flex;gap:10px}
.row>div{flex:1}
.actions{position:absolute;bottom:20px;left:16px;right:16px;display:flex;align-items:center;gap:14px}
.btn-main{flex:1;height:40px;border-radius:20px;background:var(--green);color:var(--white);font-weight:600;font-size:13px;display:flex;align-items:center;justify-content:center}
.btn-alt{width:96px;height:32px;border-radius:16px;background:var(--green);color:var(--white);font-weight:600;font-size:10px;display:flex;align-items:center;justify-content:center}
/* profile */
.hero{position:absolute;top:0;left:0;right:0;height:250px}
.hero-fill{position:absolute;inset:0;background:linear-gradient(180deg,#7d93b4 0%,#c0c9d3 35%,#547e30 65%,#3f6c1f 100%)}
.hero-nav{position:absolute;top:30px;left:14px;right:14px;display:flex;align-items:center;color:var(--white);font-size:12px;font-weight:600;gap:70px}
.hero-name{position:absolute;left:16px;bottom:80px;color:var(--white);font-weight:700;font-size:20px;display:flex;align-items:center;gap:8px}
.edit-dot{width:18px;height:18px;border-radius:50%;background:var(--white)}
.hero-addr{position:absolute;left:16px;bottom:62px;color:var(--white);font-size:9px}
.follow{position:absolute;left:16px;bottom:30px;border:1px solid var(--white);border-radius:12px;color:var(--white);font-size:9px;padding:4px 16px}
.quote-pill{position:absolute;top:228px;right:20px;background:var(--green);color:var(--white);font-size:12px;font-weight:600;border-radius:20px;padding:12px 30px}
.tabs{position:absolute;top:284px;left:14px;right:14px;display:flex;justify-content:space-between;font-size:9px;border-bottom:1px solid #ddd}
.tab{padding-bottom:6px}
.tab--active{color:var(--green);font-weight:600;border-bottom:2px solid var(--green)}
.grid{position:absolute;top:312px;left:14px;right:14px;display:grid;grid-template-columns:1fr 1fr;gap:4px}
.tile{height:96px}
.tile--a{background:linear-gradient(160deg,#8aa9c4,#4f7a2b)}
.tile--b{background:linear-gradient(160deg,#9cb4a0,#3e6d20)}
.tile--c{background:linear-gradient(180deg,#5c8f2c,#3b6a1c)}
.tile--d{background:linear-gradient(180deg,#97adc6,#4b7a28)}
.tile--e{background:linear-gradient(180deg,#a3b6cc,#5a8a30)}
.tile--f{background:linear-gradient(180deg,#6d9a36,#447322)}
</style>
</head>
<body>
<main class="stage">

  <section class="screen screen--directory" aria-label="Directory listing">
    <div class="status"><span>●●●○ FFF</span><span>100%<i class="battery"></i></span></div>
    <div class="topbar">
      <svg width="20" height="14" viewBox="0 0 20 14"><g stroke="#5f7f12" stroke-width="2"><line x1="0" y1="1" x2="20" y2="1"/><line x1="0" y1="7" x2="20" y2="7"/><line x1="0" y1="13" x2="20" y2="13"/></g></svg>
      <div class="search"><svg width="9" height="9" viewBox="0 0 10 10"><circle cx="4" cy="4" r="3" fill="none" stroke="#8a8a84"/><line x1="6.5" y1="6.5" x2="9" y2="9" stroke="#8a8a84"/></svg>Search professionals</div>
      <svg width="22" height="22" viewBox="0 0 22 22"><circle cx="11" cy="11" r="9.5" fill="none" stroke="#5f7f12" stroke-width="2"/><path d="M11 6v10M6 11h10" stroke="#5f7f12" stroke-width="2"/></svg>
    </div>

    <article class="listing listing--one">
      <div class="photo">
        <div class="photo-fill photo-fill--lawn" role="img" aria-label="Photo of a manicured lawn with palm trees in front of a large white house"></div>
        <div class="photo-title">Fernhollow Gardens</div>
        <div class="stars">★★★★★</div>
        <span class="state-pill state-pill--open">OPEN</span>
        <svg class="heart" width="16" height="14" viewBox="0 0 16 14"><path d="M8 13 1.5 6.5a3.5 3.5 0 0 1 5-5L8 3l1.5-1.5a3.5 3.5 0 0 1 5 5Z" fill="#fff"/></svg>
      </div>
      <div class="owner"><div class="avatar"></div><div><div class="owner-name">Fernhollow Gardens</div><div class="owner-role">Gardener</div></div></div>
      <p class="blurb">Professional landscaping and gardening, we undertake every gardening job.</p>
      <span class="ago">2hr ago</span>
      <span class="btn-small">Request a Quote</span>
    </article>

    <article class="listing listing--two">
      <div class="photo">
        <div class="photo-fill photo-fill--garden" role="img" aria-label="Photo of a topiary garden with clipped hedges and lavender beds"></div>
        <span class="ghost-quote">Request a Quote</span>
        <div class="photo-title">Greenrow</div>
        <div class="stars">★★★★☆</div>
        <span class="state-pill state-pill--closed">Closed</span>
        <svg class="heart" width="16" height="14" viewBox="0 0 16 14"><path d="M8 13 1.5 6.5a3.5 3.5 0 0 1 5-5L8 3l1.5-1.5a3.5 3.5 0 0 1 5 5Z" fill="none" stroke="#fff" stroke-width="1.4"/></svg>
      </div>
      <div class="owner"><div class="avatar"></div><div><div class="owner-name">Mara Quill</div><div class="owner-role">Owner</div></div></div>
      <p class="blurb">Professional landscaping and gardening, we undertake every gardening job.</p>
      <span class="ago">2hr ago</span>
    </article>

    <div class="fab"><svg width="18" height="12" viewBox="0 0 18 12"><g stroke="#fff" stroke-width="1.6"><line x1="0" y1="1" x2="18" y2="1"/><line x1="3" y1="6" x2="15" y2="6"/><line x1="6" y1="11" x2="12" y2="11"/></g></svg></div>
  </section>

  <section class="screen screen--edit" aria-label="Edit profile">
    <div class="status"><span>●●●○ FFF</span><span>100%<i class="battery"></i></span></div>
    <div class="edit-head">
      <svg width="18" height="14" viewBox="0 0 18 14"><path d="M17 7H2M7 1 1 7l6 6" fill="none" stroke="#2f2f2f" stroke-width="2"/></svg>
      <div class="edit-title">Edit Profile</div>
    </div>
    <form class="form">
      <div class="field-label">Business Name</div><div class="field">Fernhollow Gardens</div>
      <div class="field-label">Address</div><div class="field">48 Linden Row</div>
      <div class="row">
        <div><div class="field-label">City</div><div class="field">Brookvale</div></div>
        <div><div class="field-label">Zip Code</div><div class="field">90417</div></div>
      </div>
      <div class="field-label">State</div><div class="field">Oregon<span>⌄</span></div>
      <div class="field-label">Mobile Number</div><div class="field">(555) 201-330</div>
      <div class="field-label">Company Info</div><div class="field field--area"></div>
      <div class="field-label">Service Offerings (Please enter one service per line)</div><div class="field field--area"></div>
      <div class="field-label">Social Connect</div><div class="field">Social profile<span>⌄</span></div>
    </form>
    <div class="actions"><span class="btn-main">Update</span><span class="btn-alt">Connect</span></div>
  </section>

  <section class="screen screen--profile" aria-label="Business profile">
    <div class="hero">
      <div class="hero-fill" role="img" aria-label="Photo of a wide lawn with palm trees and a white mansion"></div>
      <div class="status status--light"><span>●●●○ FFF</span><span>100%<i class="battery"></i></span></div>
      <div class="hero-nav">
        <svg width="18" height="14" viewBox="0 0 18 14"><path d="M17 7H2M7 1 1 7l6 6" fill="none" stroke="#fff" stroke-width="2"/></svg>
        <span>Business Profile</span>
      </div>
      <div class="hero-name">Fernhollow Gardens<span class="edit-dot"></span></div>
      <div class="hero-addr">48 Linden Row, Vermont</div>
      <span class="follow">Follow</span>
    </div>
    <span class="quote-pill">Request a Quote</span>
    <nav class="tabs"><span class="tab tab--active">Recent Work</span><span class="tab">Services Offered</span><span class="tab">Contact Information</span></nav>
    <div class="grid">
      <div class="tile tile--a" role="img" aria-label="Photo of a ride-on lawn mower"></div>
      <div class="tile tile--b" role="img" aria-label="Photo of a garden with trees"></div>
      <div class="tile tile--c" role="img" aria-label="Photo of a freshly striped lawn"></div>
      <div class="tile tile--d" role="img" aria-label="Photo of a lawn before a white house"></div>
      <div class="tile tile--e" role="img" aria-label="Photo of palm trees and a mansion lawn"></div>
      <div class="tile tile--f" role="img" aria-label="Photo of a trimmed hedge border"></div>
    </div>
  </section>

</main>
</body>
</html>
```